KVB Website Design

We need a new home and sub page design for HelioVortek.com. The winner will be selected based upon the home page design. The sub page and drop down navigation can be completed once the project is awarded. See attachments for sitemap and photos. Below is a detailed description, with examples, of what we are looking for:

Main page design
• See Valtemi.com/usa or quorvanautos.com
• Position logo at the top-center or left
• Include phone number in header (555) 613-4871
• Main navigation centered below or to the right of logo
• Remainder of screen will be large photo slider (similar to quorvanautos.com)
• Positioned above the photo slider just below the main navigation will be a semitransparent area for Featured products listing/links; Frac Pumps, Fire Pumps, Generators, Motorcycles (see Pellarunpark.com --- similar to the “price your vacation” section)
• On scroll down there will be large product boxes for each product line. Similar to three boxes on quorvanautos.com….one box per product (Fire & Flood Control, Power Generation, Well Stimulation, Motorcycles, Speed Boats, Special Projects)
• Include bottom navigation
Main Navigation design
• See quorvanautos.com
• Like the drop down style – full bar graphic across the screen with multiple shorter columns of navigation from left to right, rather than long vertical drop downs

Internal page design
• Like interior page design on brambleworksltd.com
• Main Product category page (see http://www.brambleworksltd.com/rigs)
• Individual Product page (see http://www.brambleworksltd.com/rigs/bramble-rig-mats/)

```html
<!DOCTYPE html>
<html lang="en">
<head>
<meta charset="utf-8">
<title>KVB</title>
<link rel="stylesheet" href="https://fonts.googleapis.com/css2?family=PT+Sans:wght@400;700&family=Arimo:wght@400&display=swap">
<style>
  :root {
    --top-band: #6b6b6b;
    --nav-light: #f4f5f6;
    --nav-shade: #dcdee0;
    --nav-text: #4a4a4a;
    --feature-band: #6e6e6e;
    --slider-top: #6f6f6f;
    --slider-mid: #a9a9a9;
    --slider-floor: #e6e6e6;
    --hero-dark: #26272a;
    --hero-mid: #3a3c40;
    --white: #ffffff;
    --footer: #5b5958;
    --footer-text: #ececec;
    --footer-rule: #7a7877;
    --dot-active: #6b7fc8;
    --dot: #c4c6ca;
    --accent-yellow: #f3d21a;
    --logo-red: #d7261e;
  }
  * { margin: 0; padding: 0; box-sizing: border-box; }
  html, body { width: 914px; height: 1200px; overflow: hidden; }
  body { position: relative; background: var(--white); font-family: "PT Sans", sans-serif; }

  .top-band { position: absolute; left: 0; top: 0; width: 914px; height: 58px; background: var(--top-band); }
  .nav-band { position: absolute; left: 0; top: 58px; width: 914px; height: 73px;
    background: linear-gradient(var(--nav-light), var(--nav-shade)); border-top: 1px solid #8a8a8a; }

  .brand { position: absolute; left: 68px; top: 16px; display: flex; align-items: center; gap: 10px; }
  .brand-mark { width: 84px; height: 84px; border-radius: 50%; background: var(--accent-yellow); }
  .brand-name { font-family: "PT Sans", sans-serif; font-weight: 700; font-size: 54px; color: var(--logo-red); letter-spacing: 2px; }

  .phone { position: absolute; left: 503px; top: 21px; display: flex; align-items: center; gap: 8px;
    color: var(--white); font-size: 13.5px; }
  .search { position: absolute; left: 650px; top: 16px; width: 198px; height: 26px; background: var(--white);
    border: 1px solid #d0d0d0; display: flex; align-items: center; justify-content: space-between; padding: 0 8px 0 10px; }
  .search span { color: #8a8a8a; font-size: 11px; }

  .main-nav { position: absolute; top: 89px; left: 0; width: 914px; }
  .main-nav a { position: absolute; color: var(--nav-text); font-size: 14px; text-decoration: none; letter-spacing: -0.2px; }

  .featured { position: absolute; left: 0; top: 131px; width: 914px; height: 67px; background: var(--feature-band);
    border-bottom: 1px solid #8a8a8a; display: flex; align-items: center; justify-content: center; color: var(--white); }
  .featured-title { font-size: 15.5px; margin-right: 16px; }
  .featured a { color: var(--white); font-size: 13.5px; text-decoration: none; }
  .featured .sep { margin: 0 8px; font-size: 13px; }

  .slider { position: absolute; left: 0; top: 198px; width: 914px; height: 445px;
    background: linear-gradient(var(--slider-top) 0%, var(--slider-mid) 60%, var(--slider-floor) 78%, #f1f1f1 100%); }
  .slide-photo { position: absolute; left: 127px; top: 67px; width: 678px; height: 320px; border-radius: 6px;
    background: linear-gradient(160deg, var(--hero-mid) 0%, var(--hero-dark) 55%, #1b1c1e 100%); }
  .slider-dots { position: absolute; left: 427px; top: 411px; display: flex; gap: 4px; }
  .slider-dots i { width: 13px; height: 13px; border-radius: 50%; background: var(--dot); display: block; }
  .slider-dots i.active { background: var(--dot-active); }

  .product-box { position: absolute; top: 687px; width: 227px; height: 173px; overflow: hidden; }
  .product-box .photo { position: absolute; inset: 0; }
  .product-box .label { position: absolute; left: 0; bottom: 0; width: 100%; height: 36px; padding-left: 14px;
    background: rgba(60,60,60,0.55); color: var(--white); font-size: 15.5px; line-height: 36px; }
  .box-fire { left: 99px; }
  .box-fire .photo { background: linear-gradient(#5e86b9 0%, #9db5cf 50%, #b8a26a 78%, #8a7a5a 100%); }
  .box-power { left: 345px; }
  .box-power .photo { background: linear-gradient(#7d9fc8 0%, #c9d6e2 45%, #4f7a5e 60%, #8f8470 100%); }
  .box-well { left: 587px; }
  .box-well .photo { background: linear-gradient(#ffffff 0%, #f3f3f3 18%, #e0742a 40%, #c8602a 62%, #4a5a52 85%, #2f3434 100%); }

  .footer { position: absolute; left: 0; top: 916px; width: 914px; height: 284px; background: var(--footer); color: var(--footer-text); }
  .footer-col { position: absolute; top: 56px; }
  .footer-col h3 { font-family: "Arimo", sans-serif; font-weight: 400; font-size: 13.5px; letter-spacing: 0.2px; margin-bottom: 9px; }
  .footer-col a { display: block; color: var(--footer-text); font-size: 12px; text-decoration: none; line-height: 24.7px; }
  .follow p { font-size: 12px; line-height: 22px; width: 170px; margin-top: -2px; }
  .social { display: flex; gap: 8px; margin-top: 12px; }
  .social i { width: 23px; height: 23px; border-radius: 50%; background: var(--white); display: block; }
  .footer-rule { position: absolute; left: 66px; top: 220px; width: 752px; height: 1px; background: var(--footer-rule); }
  .copyright { position: absolute; left: 66px; top: 243px; font-family: "Arimo", sans-serif; font-size: 11.5px; color: var(--white); }
</style>
</head>
<body>
  <header>
    <div class="top-band"></div>
    <div class="nav-band"></div>
    <div class="brand"><span class="brand-mark"></span><span class="brand-name">KVB</span></div>
    <div class="phone">(555) 613-4871
      <svg width="14" height="18" viewBox="0 0 14 18" aria-hidden="true">
        <path d="M3 1 L6 1 L7 5 L5 6.5 C6 9.5 7.5 11.5 9.5 12.5 L11 10.5 L14 12 L13 16 C7 17 1 9 3 1 Z" fill="var(--accent-yellow)"/>
      </svg>
    </div>
    <div class="search"><span>Search..</span>
      <svg width="11" height="11" viewBox="0 0 11 11" aria-hidden="true">
        <circle cx="4.5" cy="4.5" r="3.5" fill="none" stroke="#999" stroke-width="1.5"/>
        <line x1="7" y1="7" x2="10.5" y2="10.5" stroke="#999" stroke-width="1.5"/>
      </svg>
    </div>
    <nav class="main-nav">
      <a style="left:399px">PRODUCTS</a>
      <a style="left:501px">ABOUT</a>
      <a style="left:578px">MEDIA</a>
      <a style="left:652px">CONTACT</a>
      <a style="left:745px">QUOTE REQUEST</a>
    </nav>
  </header>

  <section class="featured">
    <span class="featured-title">Featured Products Listing:</span>
    <a>Frac Pumps</a><span class="sep">|</span>
    <a>Fire Pumps</a><span class="sep">|</span>
    <a>Generators</a><span class="sep">|</span>
    <a>Motorcycles</a>
  </section>

  <section class="slider">
    <div class="slide-photo" role="img" aria-label="Black sport motorcycle with blue seat shown in side view"></div>
    <div class="slider-dots"><i class="active"></i><i></i><i></i><i></i></div>
  </section>

  <section class="product-lines">
    <div class="product-box box-fire">
      <div class="photo" role="img" aria-label="Fire and flood control pump spraying water"></div>
      <div class="label">Fire &amp; Flood Control</div>
    </div>
    <div class="product-box box-power">
      <div class="photo" role="img" aria-label="Green power generator unit on site"></div>
      <div class="label">Power Generation</div>
    </div>
    <div class="product-box box-well">
      <div class="photo" role="img" aria-label="Orange well stimulation equipment on a truck trailer"></div>
      <div class="label">Well Stimulation</div>
    </div>
  </section>

  <footer class="footer">
    <div class="footer-col" style="left:66px">
      <h3>PRODUCTS</h3>
      <a>Fire &amp; Flood Control</a><a>Power Generation</a><a>Well Stimulation</a><a>Recreational</a><a>Special Projects</a>
    </div>
    <div class="footer-col" style="left:249px">
      <h3>ABOUT</h3>
      <a>History</a><a>Leadership</a><a>Facilities</a><a>Careers</a>
    </div>
    <div class="footer-col" style="left:386px">
      <h3>MEDIA</h3>
      <a>News</a><a>Videos</a><a>Facilities</a><a>Careers</a>
    </div>
    <div class="footer-col" style="left:523px">
      <h3>CONTACT</h3>
      <a>History</a><a>Careers</a><a>Investors</a><a>Suppliers</a>
    </div>
    <div class="footer-col follow" style="left:664px">
      <h3>FOLLOW US</h3>
      <p>Follow us our news and events through social networks.</p>
      <div class="social"><i></i><i></i><i></i><i></i></div>
    </div>
    <div class="footer-rule"></div>
    <div class="copyright">Copyright ©2013. All Rights Reserved.</div>
  </footer>
</body>
</html>
```